New world-class investment firm needs a business card design

We need a business card design for a new investment firm called 'Vallin Soeurs & Company.' We acquire companies in the media sector and secure funding from conservative ultra, high-net worth individuals. We would like a black and white color design. We are seeking classic, elegant, and sophisticated designs. The final design should communicate financial safety, class, timelessness, and highly ethical. On the back of the business card, we would simply like the lion logo to be centered. I have attached a mock card, and variations on it are welcomed.
Conservative
- Garamond

```html
<!DOCTYPE html>
<html lang="en">
<head>
<meta charset="utf-8">
<title>Vallin Soeurs &amp; Company — Business Card</title>
<link rel="stylesheet" href="https://fonts.googleapis.com/css2?family=EB+Garamond:wght@400;500&display=swap">
<style>
  :root {
    --stage: #141414;
    --card: #ffffff;
    --ink: #1a1a1a;
    --frame-light: #e4e4e4;
    --frame-mid: #a9a9a9;
    --frame-dark: #8f8f8f;
    --watermark: #ececec;
    --mark: #222222;
  }
  * { margin: 0; padding: 0; box-sizing: border-box; }
  html, body {
    width: 1200px;
    height: 750px;
    overflow: hidden;
    background: var(--stage);
  }
  .canvas {
    position: relative;
    width: 1200px;
    height: 750px;
    background: var(--stage);
    font-family: "EB Garamond", Garamond, serif;
    color: var(--ink);
  }
  .card {
    position: absolute;
    width: 587px;
    height: 342px;
    background: var(--card);
  }
  .card--front { left: 72px; top: 30px; }
  .card--back { left: 548px; top: 389px; }

  /* striped border frame */
  .frame {
    position: absolute;
    inset: 0;
    background: repeating-linear-gradient(135deg,
      var(--frame-mid) 0 3px, var(--frame-light) 3px 6px);
  }
  .frame__inner {
    position: absolute;
    inset: 13px;
    background: var(--card);
  }
  .frame__corners {
    position: absolute;
    inset: 0;
    width: 100%;
    height: 100%;
  }
  .frame__corners polygon { fill: var(--frame-dark); }

  .watermark {
    position: absolute;
    left: 192px;
    top: 81px;
    width: 206px;
    height: 206px;
    border-radius: 50%;
    border: 3px solid var(--watermark);
  }

  .front-text {
    position: absolute;
    inset: 0;
    text-align: center;
  }
  .front-text > * {
    position: absolute;
    left: 0;
    right: 0;
    line-height: 1;
  }
  .firm-name   { top: 33px;  font-size: 25px; }
  .firm-cities { top: 66px;  font-size: 17px; }
  .person-name { top: 143px; font-size: 25px; }
  .person-role { top: 178px; font-size: 18px; }
  .contact-email { top: 243px; font-size: 19px; }
  .contact-phone { top: 292px; font-size: 16px; }

  .brand {
    position: absolute;
    inset: 0;
    display: flex;
    flex-direction: column;
    align-items: center;
    justify-content: center;
    gap: 22px;
  }
  .brand__circle {
    width: 120px;
    height: 120px;
    border-radius: 50%;
    border: 3px solid var(--mark);
  }
  .brand__name {
    font-size: 24px;
    color: var(--mark);
    line-height: 1;
  }
</style>
</head>
<body>
<main class="canvas">

  <section class="card card--front" aria-label="Business card front">
    <div class="frame">
      <div class="frame__inner"></div>
      <svg class="frame__corners" viewBox="0 0 587 342" preserveAspectRatio="none" aria-hidden="true">
        <polygon points="0,0 22,0 0,22"/>
        <polygon points="587,0 565,0 587,22"/>
        <polygon points="0,342 22,342 0,320"/>
        <polygon points="587,342 565,342 587,320"/>
      </svg>
    </div>
    <div class="watermark" aria-hidden="true"></div>
    <div class="front-text">
      <h1 class="firm-name" style="font-weight:400">Vallin Soeurs &amp; Company</h1>
      <p class="firm-cities">New York • Los Angeles • Geneva</p>
      <p class="person-name">Lucien A. Vallin</p>
      <p class="person-role">Chairman &amp; CEO</p>
      <p class="contact-email">lucien@vallinsoeurs.com</p>
      <p class="contact-phone">917.555.0142</p>
    </div>
  </section>

  <section class="card card--back" aria-label="Business card back">
    <div class="brand">
      <div class="brand__circle" aria-hidden="true"></div>
      <p class="brand__name">Vallin Soeurs &amp; Company</p>
    </div>
  </section>

</main>
</body>
</html>
```